Kestrel Lane flyer

Need a A6 size horizontal layout flyer. See attached example for ideas as well as some images I have which you can use. we are a hire car company that provides vehicles to clients who have recently been involved in car accidents and who's cars are currently getting fixed and so they lose the use of their own vehicle. see our website to keep flyer in line with website and for any further information kestrellane.com.au

Target Market(s)

people involved in not at fault car accidents

Industry/Entity Type

It Company

Requirements
Must have
• *ask people to let us know where they got our flyer from when they call us
• *call to action for people to call our phone number 1800 417 582
Should not have
• any mentioning that the vehicle is free

```html
<!DOCTYPE html>
<html lang="en">
<head>
<meta charset="utf-8">
<title>Kestrel Lane Flyer</title>
<link href="https://fonts.googleapis.com/css2?family=Lato:wght@400;700;900&family=PT+Sans+Narrow&display=swap" rel="stylesheet">
<style>
  :root {
    --blue: #3a93f5;
    --blue-deep: #1f7ae0;
    --ink: #111111;
    --text: #333333;
    --paper: #ffffff;
    --stage: #b3b3b3;
  }
  * { box-sizing: border-box; margin: 0; padding: 0; }
  html, body { width: 1200px; height: 1200px; overflow: hidden; }
  body { background: var(--stage); font-family: "Lato", sans-serif; position: relative; }

  .flyer {
    position: absolute; left: 40px; top: 203px;
    width: 1120px; height: 794px;
    background: linear-gradient(170deg, #ffffff 40%, #eef0f3 70%, #ffffff 100%);
    overflow: hidden;
  }
  .photo { position: absolute; top: 0; height: 360px; }
  .photo--car { left: 0; width: 553px; background: linear-gradient(120deg, #3d4035 0%, #8e8d86 40%, #e4e6e8 70%, #b9bdc2 100%); }
  .photo--drivers { left: 564px; width: 556px; background: linear-gradient(100deg, #5a6270 0%, #c9d3de 45%, #e9eef3 70%, #7b8594 100%); }

  .sweep { position: absolute; left: 0; top: 0; width: 1120px; height: 794px; }

  .brand {
    position: absolute; left: 0; width: 100%; top: 355px;
    text-align: center; font-weight: 900; font-size: 44px; color: var(--ink);
  }

  .step {
    position: absolute; top: 431px; width: 286px; height: 162px;
    border-radius: 14px; color: #fff; text-align: center;
    box-shadow: 6px 6px 0 #e3e5e8, 7px 8px 10px rgba(0,0,0,0.15);
    display: flex; align-items: center; justify-content: center;
  }
  .step__frame {
    position: absolute; inset: 11px; border: 1.5px solid rgba(255,255,255,0.9); border-radius: 12px;
  }
  .step__body { position: relative; display: flex; flex-direction: column; align-items: center; gap: 6px; padding: 0 14px; }
  .step--blue { background: var(--blue); }
  .step--dark { background: var(--ink); }
  .step--call { left: 44px; }
  .step--details { left: 420px; }
  .step--vehicle { left: 797px; }
  .step__line { font-size: 22px; line-height: 1.2; }
  .step__line strong { font-weight: 700; }
  .step__caps { font-weight: 700; font-size: 23px; line-height: 1.25; text-transform: uppercase; }
  .step--vehicle .step__caps { font-size: 21px; line-height: 1.2; }

  .chevron { position: absolute; top: 490px; width: 46px; height: 46px; }
  .chevron--one { left: 367px; }
  .chevron--two { left: 748px; }

  .about { position: absolute; left: 35px; top: 610px; width: 745px; }
  .about__title { color: var(--blue); font-weight: 700; font-size: 19px; margin-bottom: 4px; }
  .about__copy { font-family: "PT Sans Narrow", sans-serif; font-size: 14.2px; line-height: 18.5px; color: var(--text); }
  .about__ask { font-weight: 700; color: var(--ink); }

  .perks {
    position: absolute; left: 800px; top: 628px; width: 320px; height: 103px;
    background: var(--ink); clip-path: polygon(0 0, 290px 0, 100% 6%, 100% 94%, 290px 100%, 0 100%);
  }
  .perk { position: absolute; left: 26px; display: flex; align-items: center; gap: 22px; color: #fff; font-size: 25px; }
  .perk--delivery { top: 12px; }
  .perk--new { top: 58px; }
  .perk__badge { width: 52px; height: 24px; background: var(--blue); border-radius: 3px; color: var(--ink); font-size: 17px; font-weight: 700; display: flex; align-items: center; justify-content: center; }

  .cta { position: absolute; left: 35px; top: 737px; display: flex; align-items: baseline; gap: 14px; }
  .cta__line { font-size: 28px; font-weight: 700; color: var(--ink); }
  .cta__number { color: var(--blue); }
  .cta__web { font-size: 19px; letter-spacing: 1.5px; color: var(--ink); display: flex; align-items: center; gap: 8px; }

  .base-band { position: absolute; left: 0; bottom: 0; width: 100%; height: 16px; background: var(--ink); border-radius: 12px 12px 0 0; }
</style>
</head>
<body>
<main class="flyer">
  <div class="photo photo--car" role="img" aria-label="Close-up of a white car's headlight beside a shaded dirt road"></div>
  <div class="photo photo--drivers" role="img" aria-label="Smiling couple seated in a car, man at the wheel"></div>

  <svg class="sweep" viewBox="0 0 1120 794" aria-hidden="true">
    <defs>
      <linearGradient id="sheen" x1="0" y1="0" x2="1" y2="1">
        <stop offset="0" stop-color="#ffffff"/>
        <stop offset="0.6" stop-color="#eceef1"/>
        <stop offset="1" stop-color="#ffffff"/>
      </linearGradient>
    </defs>
    <path d="M0 318 Q560 160 1120 358 L1120 794 L0 794 Z" fill="var(--blue)"/>
    <path d="M0 352 Q560 215 1120 390 L1120 794 L0 794 Z" fill="url(#sheen)"/>
  </svg>

  <h1 class="brand">Kestrel Lane</h1>

  <section class="step step--blue step--call">
    <span class="step__frame"></span>
    <div class="step__body">
      <svg width="34" height="34" viewBox="0 0 24 24" fill="none" stroke="#fff" stroke-width="2" stroke-linecap="round" stroke-linejoin="round"><path d="M5 3h4l2 5-2.5 1.5a11 11 0 0 0 6 6L16 13l5 2v4a2 2 0 0 1-2 2A17 17 0 0 1 3 5a2 2 0 0 1 2-2z" fill="#fff"/><path d="M15 3a6 6 0 0 1 6 6M15 7a2 2 0 0 1 2 2"/></svg>
      <p class="step__line">Call us on <strong>1800 417 582</strong></p>
      <p class="step__caps">Free Call</p>
    </div>
  </section>

  <svg class="chevron chevron--one" viewBox="0 0 46 46" aria-hidden="true"><path d="M4 4h18l20 19-20 19H4l20-19z" fill="var(--blue)" stroke="var(--ink)" stroke-width="2"/></svg>

  <section class="step step--dark step--details">
    <span class="step__frame"></span>
    <div class="step__body">
      <svg width="40" height="36" viewBox="0 0 30 26" fill="none" stroke="#fff" stroke-width="1.5" stroke-linecap="round" stroke-linejoin="round"><path d="M3 8h4l1.5 4-2 1.2a9 9 0 0 0 5 5L13 16l4 1.5v3.5a1.5 1.5 0 0 1-1.5 1.5A13 13 0 0 1 1.5 9.5 1.5 1.5 0 0 1 3 8z"/><path d="M20 2a7 6 0 1 1-4 11l-3 1 1-3A7 6 0 0 1 20 2z"/><circle cx="17.5" cy="8" r=".6" fill="#fff"/><circle cx="20" cy="8" r=".6" fill="#fff"/><circle cx="22.5" cy="8" r=".6" fill="#fff"/></svg>
      <p class="step__caps">Provide<br>Accident Details</p>
    </div>
  </section>

  <svg class="chevron chevron--two" viewBox="0 0 46 46" aria-hidden="true"><path d="M4 4h18l20 19-20 19H4l20-19z" fill="var(--blue)" stroke="var(--ink)" stroke-width="2"/></svg>

  <section class="step step--blue step--vehicle">
    <span class="step__frame"></span>
    <div class="step__body">
      <svg width="50" height="30" viewBox="0 0 50 30" fill="none" stroke="#fff" stroke-width="2" stroke-linejoin="round"><path d="M3 20v-6l6-2 6-8h16l8 8 7 2v6H3z"/><path d="M17 6l-4 6h24l-6-6z"/><circle cx="13" cy="21" r="4" fill="var(--blue)"/><circle cx="37" cy="21" r="4" fill="var(--blue)"/></svg>
      <p class="step__caps">You get a replace-<br>ment vehicle we take<br>care of the rest</p>
    </div>
  </section>

  <article class="about">
    <h2 class="about__title">Accident Replacement Vehicle</h2>
    <p class="about__copy">Throughout Australia, there are a lot of people on the roads, especially in the main cities like Sydney and Melbourne. It's not uncommon to get into a car accident. Whether it's a simple fender bender or something more severe, your car could end up in a repair shop for repairs. The biggest problem that you now have to deal with is that while your vehicle is in the repair shop, you have no car. If the accident wasn't your fault, an accident replacement vehicle is available to you. You can call and schedule this replacement car so that you are not left without a car while it is under repairs. <span class="about__ask">When you call, please let us know where you got this flyer.</span></p>
  </article>

  <aside class="perks">
    <div class="perk perk--delivery">
      <svg width="56" height="34" viewBox="0 0 56 34" fill="none" stroke="var(--blue)" stroke-width="2" stroke-linejoin="round"><rect x="2" y="3" width="34" height="22"/><path d="M36 10h10l7 8v7H36z"/><circle cx="12" cy="27" r="4" fill="var(--ink)"/><circle cx="44" cy="27" r="4" fill="var(--ink)"/><text x="5" y="19" fill="var(--blue)" stroke="none" font-family="Lato, sans-serif" font-weight="900" font-size="11">FREE</text></svg>
      <span>Free Delivery</span>
    </div>
    <div class="perk perk--new">
      <span class="perk__badge">new</span>
      <span>New Vehicles</span>
    </div>
  </aside>

  <footer class="cta">
    <p class="cta__line">Call our phone number <span class="cta__number">1800 417 582</span></p>
    <p class="cta__web">
      <svg width="14" height="14" viewBox="0 0 14 14" aria-hidden="true"><circle cx="7" cy="7" r="6" fill="var(--blue)"/><path d="M1 7h12M7 1c-3 3-3 9 0 12M7 1c3 3 3 9 0 12" stroke="#fff" stroke-width="1" fill="none"/></svg>
      www.kestrellane.com.au
    </p>
  </footer>

  <div class="base-band"></div>
</main>
</body>
</html>
```